Updated business card

I would like to change the picture on the existing design. Please use the attached photo. Remove my last name from the logo and have that appear (just my first name with the lock symbol [trademarked]) appear horizontally or vertically? on the front of the card. My company information has changed on the back of the card. It should be "Lantern" instead of "Harborline 88 Oakmont Realty", 4720 Fenwick Blvd. Arlington, VA 22207 is the new address. The Harborline 88 Oakmont logo should be replaced with the Lantern logo which is attached as well. I am using Pixo cards with the rounded edges for printing so the size is larger than the typically business card. The colors should remain consistent with what I have but can be used differently.

```html
<!DOCTYPE html>
<html lang="en">
<head>
<meta charset="utf-8">
<title>Marisela Thorne — Business Card</title>
<link href="https://fonts.googleapis.com/css2?family=Montserrat:wght@400;500;600&display=swap" rel="stylesheet">
<style>
  :root{
    --page:#e9e6e2;
    --ink:#0d0d0e;
    --ink-soft:#2a2a2d;
    --band:#060607;
    --magenta:#d11c93;
    --white:#f4f4f4;
    --muted:#bdbdbd;
    --photo-warm:#a8593a;
    --photo-light:#d9d9d9;
  }
  *{box-sizing:border-box;margin:0;padding:0}
  html,body{width:771px;height:1200px;overflow:hidden;background:var(--page)}
  .canvas{position:relative;width:771px;height:1200px}
  .card{
    position:absolute;top:302px;width:340px;height:595px;border-radius:20px;overflow:hidden;
    background:linear-gradient(160deg,var(--ink-soft) 0%,var(--ink) 55%,#050506 100%);
    box-shadow:0 10px 30px rgba(0,0,0,.25);
    font-family:"Montserrat",sans-serif;color:var(--white);
  }
  .card--contact{left:30px}
  .card--portrait{left:401px}

  /* contact side */
  .brand{position:absolute;top:62px;left:0;right:0;text-align:center}
  .brand__name{font-size:31px;font-weight:500;letter-spacing:3px;color:var(--magenta)}
  .spine{position:absolute;left:22px;top:160px;width:34px;height:435px;background:var(--band)}
  .contact-panel{position:absolute;left:22px;right:0;top:160px;bottom:0;border-top:14px solid var(--band)}
  .contact-list{position:absolute;top:190px;left:22px;right:16px;list-style:none}
  .contact-item{display:flex;align-items:flex-start;height:64px}
  .contact-item__icon{width:48px;height:44px;background:var(--magenta);display:flex;align-items:center;justify-content:center;flex:none}
  .contact-item__body{padding:8px 0 0 14px;min-width:0}
  .contact-item__text{font-size:13px;line-height:1.3;color:var(--white);white-space:nowrap}
  .contact-item__rule{width:72px;height:2px;background:var(--magenta);margin-top:8px}
  .footer{position:absolute;left:70px;right:26px;bottom:36px;display:flex;align-items:center;justify-content:space-between}
  .wordmark{font-size:18px;font-weight:500;letter-spacing:5px;color:var(--white)}
  .badge{width:40px;height:38px;border:3px solid var(--white);border-radius:3px}

  /* portrait side */
  .portrait{position:absolute;top:0;left:0;right:0;height:450px;
    background:linear-gradient(180deg,var(--photo-light) 0%,#c9a18c 40%,var(--photo-warm) 75%,#5a3a2e 100%)}
  .nameplate{position:absolute;left:0;right:0;bottom:0;height:145px;background:linear-gradient(180deg,#111 0%,var(--band) 100%);padding:40px 22px 0}
  .nameplate__name{font-size:17px;font-weight:600;letter-spacing:1.5px;white-space:nowrap}
  .nameplate__creds{font-size:11px;font-weight:400;letter-spacing:1px;color:var(--muted)}
  .nameplate__title{font-size:15px;letter-spacing:2px;color:var(--magenta);margin-top:8px}
</style>
</head>
<body>
<main class="canvas">

  <section class="card card--contact">
    <header class="brand">
      <div class="brand__name">MARISELA</div>
    </header>
    <div class="contact-panel"></div>
    <div class="spine"></div>
    <ul class="contact-list">
      <li class="contact-item">
        <span class="contact-item__icon"><svg width="20" height="20" viewBox="0 0 24 24" fill="#fff"><path d="M3 9c0-3 4-5 9-5s9 2 9 5v2h-5V8.5c-2-.7-6-.7-8 0V11H3z"/><path d="M5 13h14l1 7H4z"/><circle cx="12" cy="16.5" r="2" fill="#d11c93"/></svg></span>
        <div class="contact-item__body"><div class="contact-item__text">202.555.0148</div><div class="contact-item__rule"></div></div>
      </li>
      <li class="contact-item">
        <span class="contact-item__icon"><svg width="20" height="16" viewBox="0 0 24 18" fill="none" stroke="#fff" stroke-width="2"><rect x="1" y="1" width="22" height="16"/><path d="M1 1l11 9 11-9"/></svg></span>
        <div class="contact-item__body"><div class="contact-item__text">Marisela@MariselaThorne.com</div><div class="contact-item__rule"></div></div>
      </li>
      <li class="contact-item">
        <span class="contact-item__icon"><svg width="20" height="20" viewBox="0 0 24 24" fill="none" stroke="#fff" stroke-width="1.8"><circle cx="12" cy="12" r="10"/><ellipse cx="12" cy="12" rx="4.5" ry="10"/><path d="M2 12h20M4 7h16M4 17h16"/></svg></span>
        <div class="contact-item__body"><div class="contact-item__text">MariselaThorne.com</div><div class="contact-item__rule"></div></div>
      </li>
      <li class="contact-item">
        <span class="contact-item__icon"><svg width="16" height="22" viewBox="0 0 16 22" fill="#fff"><path d="M8 0a8 8 0 0 1 8 8c0 6-8 14-8 14S0 14 0 8a8 8 0 0 1 8-8z"/><circle cx="8" cy="8" r="3" fill="#d11c93"/></svg></span>
        <div class="contact-item__body"><div class="contact-item__text">4720 Fenwick Blvd.<br>Arlington, VA 22207</div></div>
      </li>
    </ul>
    <footer class="footer">
      <span class="wordmark">LANTERN</span>
      <span class="badge"></span>
    </footer>
  </section>

  <section class="card card--portrait">
    <div class="portrait" role="img" aria-label="Portrait photo of the realtor"></div>
    <div class="nameplate">
      <div class="nameplate__name">MARISELA THORNE, <span class="nameplate__creds">J.D., LL.M.</span></div>
      <div class="nameplate__title">REALTOR</div>
    </div>
  </section>

</main>
</body>
</html>
```